New business card design needed for Trucking/Staffing company!

I am looking for a business card design. The business name is Harbor Lane Freightworks, LLC. This company is a staffing company for commercial drivers/truck drivers. Most of our customers are trucking/supply companies. Our colors are blue/black/white/grey. The info I have on my current business cards is
-Spot for a name
-2 lines for an address
-3 lines for Office, cell, and fax
-email
-website(currently on backside of card with logo but can go anywhere)
Updates

Project Deadline Extended
Reason: Open to more designs

Target Market(s)

Trucking companies, building supply companies

Industry/Entity Type

Business

Contact Information for Business Card

Edgy but professional

Font styles to use
Other font styles liked:
• Open to suggestions

Colors
0555a3
000000
ffffff
9d9d9d

Requirements
Must have
• Must have the logo incorporated

```html
<!DOCTYPE html>
<html lang="en">
<head>
<meta charset="utf-8">
<title>Harbor Lane Freightworks — Business Cards</title>
<link href="https://fonts.googleapis.com/css2?family=Open+Sans:wght@400;600;700&display=swap" rel="stylesheet">
<style>
  :root {
    --brand-blue: #283a8f;
    --mark-blue: #2b3d96;
    --rule-dark: #3a3a3c;
    --paper: #ffffff;
    --ink-grey: #8c8c8c;
    --rule-grey: #c9c9c9;
    --backdrop: #e9e9eb;
  }
  * { margin: 0; padding: 0; box-sizing: border-box; }
  html, body {
    width: 1200px; height: 900px; overflow: hidden;
    background: var(--backdrop);
    font-family: "Open Sans", Arial, sans-serif;
  }
  .canvas { position: relative; width: 1200px; height: 900px; }

  .card {
    position: absolute;
    background: var(--paper);
    box-shadow: 0 4px 14px rgba(0,0,0,0.12);
    overflow: hidden;
  }
  .card--front { left: 237px; top: 62px; width: 556px; height: 342px; }
  .card--back  { left: 457px; top: 518px; width: 560px; height: 343px; }

  .wordmark {
    position: absolute;
    display: flex; align-items: center; gap: 10px;
    color: var(--mark-blue);
    font-weight: 700;
    font-size: 25px;
    letter-spacing: 0.5px;
    white-space: nowrap;
  }
  .wordmark__dot {
    width: 14px; height: 14px; border-radius: 50%;
    background: var(--mark-blue);
  }
  .card--front .wordmark { left: 50%; top: 86px; transform: translateX(-50%); }
  .card--back  .wordmark { left: 50%; top: 142px; transform: translateX(-50%); }

  .card__rule {
    position: absolute; left: 0; right: 0; top: 179px; height: 6px;
    background: var(--rule-dark);
  }
  .card__band {
    position: absolute; left: 0; right: 0; top: 192px; bottom: 0;
    background: var(--brand-blue);
  }
  .holder-name {
    position: absolute; left: 83px; top: 257px;
    color: var(--paper); font-weight: 600; font-size: 18px;
  }
  .contact-list {
    position: absolute; left: 280px; top: 207px;
    list-style: none;
  }
  .contact-list li {
    display: flex; align-items: center; gap: 9px;
    height: 23.2px;
    color: var(--paper); font-size: 15px;
  }
  .contact-list svg { width: 10px; height: 10px; fill: var(--paper); flex: none; }

  .address-line {
    position: absolute; left: 0; right: 0; top: 284px;
    display: flex; align-items: center; justify-content: center; gap: 14px;
    color: var(--ink-grey); font-size: 14px;
  }
  .address-line::before, .address-line::after {
    content: ""; width: 60px; height: 1px; background: var(--rule-grey);
  }
</style>
</head>
<body>
<main class="canvas">

  <section class="card card--front" aria-label="Card front">
    <div class="wordmark"><span class="wordmark__dot"></span>HARBOR LANE FREIGHTWORKS</div>
    <div class="card__rule"></div>
    <div class="card__band"></div>
    <p class="holder-name">Daniel Reyes</p>
    <ul class="contact-list">
      <li><svg viewBox="0 0 10 10"><path d="M2.5 0h5a1 1 0 0 1 1 1v8a1 1 0 0 1-1 1h-5a1 1 0 0 1-1-1V1a1 1 0 0 1 1-1zm0 1.5v6h5v-6z"/></svg>044-555-0182</li>
      <li><svg viewBox="0 0 10 10"><path d="M2 0.5l1.8 2-1 1.2a6 6 0 0 0 3.5 3.5l1.2-1 2 1.8-1.2 1.5C4.5 9.5 0.5 5.5 0.5 1.7z"/></svg>123-555-0147</li>
      <li><svg viewBox="0 0 10 10"><path d="M3 0h4v3H3zM1 3.5h8v6H1zm2 2v1h1v-1zm2 0v1h1v-1zm2 0v1h1v-1z"/></svg>123-555-0196</li>
      <li><svg viewBox="0 0 10 10"><path d="M0 2h10v6H0zm0.8 0.6L5 5.6l4.2-3z" fill-rule="evenodd"/></svg>info@harborlanefreight.com</li>
      <li><svg viewBox="0 0 10 10"><path d="M5 0a5 5 0 1 0 0 10A5 5 0 0 0 5 0zm0 1c.6.6 1 1.6 1.2 2.5H3.8C4 2.6 4.4 1.6 5 1zM1.2 4.5h2.5v1H1.2zm5 0h2.6v1H6.2zM3.8 6.5h2.4C6 7.4 5.6 8.4 5 9c-.6-.6-1-1.6-1.2-2.5z"/></svg>www.harborlanefreight.com</li>
    </ul>
  </section>

  <section class="card card--back" aria-label="Card back">
    <div class="wordmark"><span class="wordmark__dot"></span>HARBOR LANE FREIGHTWORKS</div>
    <p class="address-line">12345, Address Goes Here Country Name, 123456.</p>
  </section>

</main>
</body>
</html>
```